Velmora Biz Card 2019

New business card for Velmora Property Inspections. We are a residential home inspection company in Arizona.

Target Market(s)

Real Estate

Font styles to use
Sans Serif

Requirements
Must have
• Glen Mirewick
• Home Inspector
• Velmora Property Inspections, LLC
• 480-555-0172
• glen@velmora-llc.example

```html
<!DOCTYPE html>
<html lang="en">
<head>
<meta charset="utf-8">
<title>Velmora Biz Card 2019</title>
<link href="https://fonts.googleapis.com/css2?family=Montserrat:wght@400;500;600;700&display=swap" rel="stylesheet">
<style>
  :root {
    --page-bg: #2a2d31;
    --card-bg: #1f1d1e;
    --brand-green: #3fbb3f;
    --text-white: #f2f2f2;
    --text-grey: #b9b9b9;
  }
  * { box-sizing: border-box; margin: 0; padding: 0; }
  html, body {
    width: 1200px;
    height: 900px;
    overflow: hidden;
    background: var(--page-bg);
    font-family: "Montserrat", sans-serif;
  }
  .card-set {
    position: absolute;
    inset: 0;
    display: flex;
    align-items: center;
    justify-content: center;
    gap: 40px;
  }
  .card {
    width: 540px;
    height: 309px;
    background: var(--card-bg);
    position: relative;
    box-shadow: 0 12px 30px rgba(0,0,0,0.45);
  }
  .card-back {
    display: flex;
    align-items: center;
    justify-content: center;
  }
  .back-wordmark {
    color: var(--brand-green);
    font-weight: 700;
    font-size: 44px;
    letter-spacing: 6px;
  }
  .contact-email {
    position: absolute;
    left: 34px;
    top: 40px;
    display: flex;
    align-items: center;
    gap: 10px;
    color: var(--text-grey);
    font-size: 12.5px;
  }
  .identity {
    position: absolute;
    left: 250px;
    top: 34px;
    width: 260px;
    text-align: center;
  }
  .wordmark {
    color: var(--text-white);
    font-weight: 700;
    font-size: 22px;
    letter-spacing: 2px;
  }
  .company-name {
    color: var(--text-grey);
    font-weight: 600;
    font-size: 10.5px;
    letter-spacing: 1px;
    margin-top: 6px;
  }
  .person-name {
    color: var(--text-white);
    font-weight: 700;
    font-size: 19px;
    letter-spacing: 0.5px;
    margin-top: 18px;
  }
  .person-title {
    color: var(--brand-green);
    font-size: 12px;
    letter-spacing: 1px;
    margin-top: 4px;
  }
  .contact-line {
    display: flex;
    align-items: center;
    justify-content: center;
    gap: 9px;
    color: var(--text-white);
    font-size: 12.5px;
    letter-spacing: 1.5px;
  }
  .contact-phone { margin-top: 14px; }
  .contact-address {
    position: absolute;
    left: 220px;
    width: 310px;
    bottom: 44px;
    letter-spacing: 0.5px;
  }
  .icon { width: 13px; height: 13px; flex: none; }
</style>
</head>
<body>
  <main class="card-set">
    <section class="card card-back">
      <span class="back-wordmark">VELMORA</span>
    </section>

    <section class="card card-front">
      <div class="contact-email">
        <svg class="icon" viewBox="0 0 16 12"><rect x="0" y="0" width="16" height="12" fill="#3fbb3f"/><path d="M1 1 L8 7 L15 1" stroke="#1f1d1e" stroke-width="1.5" fill="none"/></svg>
        <span>glen@velmora-llc.example</span>
      </div>

      <div class="identity">
        <div class="wordmark">VELMORA</div>
        <div class="company-name">Velmora Property Inspections, LLC</div>
        <div class="person-name">Glen Mirewick</div>
        <div class="person-title">Home Inspector</div>
        <div class="contact-line contact-phone">
          <svg class="icon" viewBox="0 0 16 16"><path d="M3 1 L6 1 L7 5 L5 6.5 C6 9 7 10 9.5 11 L11 9 L15 10 L15 13 C15 14 14 15 13 15 C6.5 15 1 9.5 1 3 C1 2 2 1 3 1 Z" fill="#3fbb3f"/></svg>
          <span>480-555-0172</span>
        </div>
      </div>

      <div class="contact-line contact-address">
        <svg class="icon" viewBox="0 0 12 16"><path d="M6 0 C2.7 0 0 2.6 0 5.8 C0 10 6 16 6 16 C6 16 12 10 12 5.8 C12 2.6 9.3 0 6 0 Z" fill="#3fbb3f"/><circle cx="6" cy="6" r="2.3" fill="#1f1d1e"/></svg>
        <span>4410 S. Harlow Ave. Dunmere, AZ 85099</span>
      </div>
    </section>
  </main>
</body>
</html>
```